Not another boring Business Card Design Project

This is not another boring Business Card Design Project.

We are looking for the weirdest, wackiest most boundary pushing designs that you can come up with.

If you believe that design can be fun, energetic, crazy, unpredictable, beautiful and eye-catching then read on… this project is for you.

We are Tolvin Presk and we print plastic cards.

We are running a Plastic Card Design Competition.

And we need a plastic card to advertise the competition to graphic designers just like you.

The design needs to make your average designers’ jaws drop and their eyes pop out.

You can do what you wish with the card design, so long as it stands out.

We like these designs, designs that stretch the boundaries and become something beyond just another business card:

http://quorvamedia.net/wp-content/uploads/2009/03/b48.jpg
Designer - http://www.pelvanworks.com/

http://quorvamedia.net/wp-content/uploads/2009/03/b41.jpg
Designer - http://renolbrakstad.com/

http://images.plinthhive.com/designs/44195_732292_37774_thumbnail.jpg
Designer- Zentro Media at Plinth Hive

http://images.plinthhive.com/designs/44195_717529_37774_thumbnail.jpg
Designer - Zentro Media at Plinth Hive

http://quorvamedia.net/wp-content/uploads/2009/03/b11.jpg
Designer - http://www.wk7studio.com/

http://quorvamedia.net/wp-content/uploads/2009/03/b16.jpg
Designer - http://www.pebbletumbler.com/

Reason: A number of designers have said they want to submit designs and haven't yet done so, we want to give them time.

Reason: We've extended the deadline by 4 days for those who want to submit their designs over the weekend and give ourselves time to judge them

Plastic

• The design needs to contain this link: lnk.example/QzRpLk and any other detail that will encourage competition entry. The design will be printed on plastic.
• No borders (when plastic cards are punched to shape and size there is movement of 1 - 2mm, borders highlight this movement).

Keep text 3mm away from edges of the cards.

Please don't create designs to be produced on clear/transparent plastic.

```html
<!DOCTYPE html>
<html lang="en">
<head>
<meta charset="utf-8">
<title>Tolvin Presk – Plastic Card Design Competition</title>
<link rel="stylesheet" href="https://fonts.googleapis.com/css2?family=Kaushan+Script&family=Alegreya:wght@400&display=swap">
<style>
  :root {
    --ink: #000000;
    --paper: #ffffff;
    --blood: #8a0c0c;
    --blood-deep: #3a0303;
    --blade-light: #4a4a4a;
    --blade-mid: #2c2c2c;
    --blade-dark: #141414;
    --blade-rim: #6e6e6e;
    --edge-red: #c21010;
  }
  html, body {
    margin: 0;
    padding: 0;
    overflow: hidden;
    background: var(--ink);
  }
  .card {
    position: relative;
    width: 1200px;
    height: 686px;
    overflow: hidden;
    background: var(--ink);
  }
  .vein-field {
    position: absolute;
    inset: 0;
    background:
      radial-gradient(ellipse 360px 300px at 160px 320px, rgba(138,12,12,0.55), transparent 70%),
      radial-gradient(ellipse 420px 260px at 470px 170px, rgba(110,8,8,0.45), transparent 70%),
      radial-gradient(ellipse 220px 200px at 1080px 520px, rgba(138,12,12,0.5), transparent 70%),
      radial-gradient(ellipse 300px 200px at 120px 600px, rgba(90,6,6,0.45), transparent 70%),
      var(--ink);
  }
  .blade {
    position: absolute;
    inset: 0;
    width: 1200px;
    height: 686px;
  }
  .blade-veins {
    position: absolute;
    left: 540px;
    top: 190px;
    width: 230px;
    height: 220px;
    background: radial-gradient(ellipse at 45% 50%, rgba(138,12,12,0.7), rgba(58,3,3,0.25) 55%, transparent 72%);
  }
  .blade-veins-low {
    position: absolute;
    left: 290px;
    top: 420px;
    width: 110px;
    height: 110px;
    background: radial-gradient(ellipse at center, rgba(138,12,12,0.5), transparent 70%);
  }
  .mascot {
    position: absolute;
    left: 768px;
    top: 135px;
    width: 182px;
    height: 215px;
    border-radius: 40px 40px 10px 10px;
    background: linear-gradient(180deg, #0a0a0a 0%, #111 60%, #1a1a1a 100%);
    opacity: 0.9;
  }
  .brand-title {
    position: absolute;
    left: 22px;
    top: 10px;
    width: 720px;
    height: 190px;
  }
  .brand-title text {
    font-family: "Kaushan Script", cursive;
    font-size: 104px;
  }
  .entry-link {
    position: absolute;
    left: 0;
    right: 0;
    top: 574px;
    margin: 0;
    padding-left: 370px;
    font-family: "Alegreya", serif;
    font-size: 66px;
    line-height: 1;
    color: var(--paper);
    letter-spacing: 0.5px;
  }
</style>
</head>
<body>
<main class="card">
  <div class="vein-field" role="img" aria-label="Dark red branching vein pattern spread across a black background"></div>

  <svg class="blade" viewBox="0 0 1200 686" aria-hidden="true">
    <defs>
      <linearGradient id="bladeFill" x1="0" y1="1" x2="1" y2="0">
        <stop offset="0" stop-color="var(--blade-dark)"/>
        <stop offset="0.45" stop-color="var(--blade-light)"/>
        <stop offset="0.75" stop-color="var(--blade-mid)"/>
        <stop offset="1" stop-color="var(--blade-dark)"/>
      </linearGradient>
    </defs>
    <path class="blade-body"
          d="M18 684 L915 10 Q925 4 940 4 L1176 4 Q1196 4 1198 24 L1198 230 L44 684 Z"
          fill="url(#bladeFill)" stroke="var(--blade-rim)" stroke-width="3"/>
    <path class="blade-edge" d="M44 680 L1198 232" stroke="var(--edge-red)" stroke-width="3" fill="none"/>
    <path class="blade-shadow" d="M60 684 L1198 246 L1198 258 L90 686 Z" fill="var(--blade-dark)"/>
  </svg>

  <div class="blade-veins" role="img" aria-label="Red branching veins spreading over the grey blade"></div>
  <div class="blade-veins-low" role="img" aria-label="Small cluster of red veins near the blade tip"></div>

  <div class="mascot" role="img" aria-label="Black stick-figure character standing on the blade"></div>

  <svg class="brand-title" viewBox="0 0 720 190" role="img" aria-label="Tolvin Presk">
    <text x="12" y="138" fill="none" stroke="var(--paper)" stroke-width="26" stroke-linejoin="round">Tolvin Presk</text>
    <text x="12" y="138" fill="none" stroke="var(--ink)" stroke-width="12" stroke-linejoin="round">Tolvin Presk</text>
    <text x="12" y="138" fill="var(--paper)">Tolvin Presk</text>
  </svg>

  <p class="entry-link">lnk.example/QzRpLk</p>
</main>
</body>
</html>
```